Innovative healthcare collaborative needs new look for business cards

CareLoomQ is a new kind of healthcare relationship company focused on aligning partners, innovation and solutions to provide needed health services to healthcare systems, hospitals or private business. Not mired in the old merger and acquisition fee-for-service framework, we focus on primary, secondary and tertiary service area partnership collaboratives. These networks are constructed by aligning healthcare services along a network of care, not just an individual patient care plan. This involves partnership arrangements with large or small medical centers, physician groups, allied health services, public health agencies, health insurers, et al as well as civic agencies, schools, farmers, supply chains to bring about needed healthcare solutions for patients. Think Amber Fields. AF does for communities what we do for hospitals and health systems. We educate and instruct on strategic, operational, and innovative solutions for a healthcare provider, practice, business, or system resulting in successful construction of care networks (legal entity). We provide the blueprint of how to do this type of partnership, focused on what’s best for the sustainability of the business and the people (patients or potential patients) living there. Rural hospitals in particular are at risk.
We also provide seminars to academic, medical academic, and private industry to instruct on how to construct these care networks and educate on the essential criteria to be successful in the new healthcare era. We have been doing this work for the past 8 years, and since COVID-19, the recognition of fractured processes has boosted the demand. We need a business card that sets the tone that the traditional healthcare delivery system in the US has transformed (overnight). Our company is educating on how to transition current business models to the new world order in this space.
Brainstormed some business card tag lines for consideration:
CareLoomQ
• A CARE NETWORK COMPANY
• allbettertogether
• connecting for the greater good

Target Market(s)

Health systems, hospitals, physician practices, academic medical schools, residency programs

Industry/Entity Type

Healthcare

Contact Information for Business Card

Doreen Vasquell, Chief Relationship Officer
doreenvasquell@mailbrook.example
mobile: 412-806-2394

Font styles to use
Serif
Sans Serif

Requirements
Should not have
• Do not use word Consultant

```html
<!DOCTYPE html>
<html lang="en">
<head>
<meta charset="utf-8">
<title>CareLoomQ Business Card</title>
<link rel="stylesheet" href="https://fonts.googleapis.com/css2?family=Arimo:wght@400;700&display=swap">
<style>
  :root {
    --backdrop: #e6e6e6;
    --brand-blue: #05587e;
    --brand-green: #a5c419;
    --paper: #ffffff;
    --card-shadow: rgba(0, 0, 0, 0.35);
  }
  * { margin: 0; padding: 0; box-sizing: border-box; }
  html, body {
    width: 1200px;
    height: 900px;
    overflow: hidden;
    background: var(--backdrop);
    font-family: "Arimo", Arial, sans-serif;
  }
  .stage {
    position: relative;
    width: 1200px;
    height: 900px;
  }
  .card {
    position: absolute;
    top: 216px;
    width: 309px;
    height: 501px;
    box-shadow: 2px 3px 4px var(--card-shadow);
  }
  .card-front {
    left: 279px;
    background: var(--brand-blue);
    border-radius: 0 66px 0 66px;
  }
  .card-back {
    left: 617px;
    background: var(--paper);
    border-radius: 66px 0 66px 0;
  }
  .wordmark {
    position: absolute;
    display: flex;
    align-items: center;
    gap: 8px;
    font-weight: 400;
    font-size: 42px;
    letter-spacing: 0.5px;
    white-space: nowrap;
  }
  .wordmark-dot {
    width: 14px;
    height: 14px;
    border-radius: 50%;
    background: var(--brand-green);
    flex: none;
  }
  .card-front .wordmark {
    left: 24px;
    top: 366px;
    color: var(--paper);
  }
  .tagline {
    position: absolute;
    left: 0;
    right: 0;
    top: 436px;
    text-align: center;
    color: var(--brand-green);
    font-weight: 700;
    font-size: 14px;
    letter-spacing: 0.3px;
  }
  .card-back .wordmark {
    left: 32px;
    top: 158px;
    color: var(--brand-blue);
  }
  .contact {
    position: absolute;
    left: 31px;
    top: 346px;
    color: var(--brand-blue);
  }
  .contact-name {
    color: var(--brand-green);
    font-weight: 700;
    font-size: 19px;
    line-height: 22px;
  }
  .contact-title {
    font-size: 15px;
    line-height: 20px;
  }
  .contact-lines {
    margin-top: 24px;
    list-style: none;
    font-size: 14.5px;
    line-height: 20px;
  }
  .contact-lines li {
    display: flex;
    align-items: center;
    gap: 6px;
  }
  .contact-icon {
    width: 14px;
    height: 14px;
    flex: none;
  }
</style>
</head>
<body>
<main class="stage">
  <section class="card card-front">
    <div class="wordmark"><span class="wordmark-dot"></span>CareLoomQ</div>
    <p class="tagline">A CARE NETWORK COMPANY</p>
  </section>

  <section class="card card-back">
    <div class="wordmark"><span class="wordmark-dot"></span>CareLoomQ</div>
    <div class="contact">
      <p class="contact-name">Doreen Vasquell</p>
      <p class="contact-title">Chief Relationship Officer</p>
      <ul class="contact-lines">
        <li>
          <svg class="contact-icon" viewBox="0 0 24 24" aria-hidden="true">
            <path fill="var(--brand-green)" d="M6.6 10.8a15.1 15.1 0 0 0 6.6 6.6l2.2-2.2c.3-.3.7-.4 1-.2 1.1.4 2.3.6 3.6.6.6 0 1 .4 1 1V20c0 .6-.4 1-1 1A17 17 0 0 1 3 4c0-.6.4-1 1-1h3.5c.6 0 1 .4 1 1 0 1.3.2 2.5.6 3.6.1.3 0 .7-.2 1z"/>
          </svg>
          412-806-2394
        </li>
        <li>
          <svg class="contact-icon" viewBox="0 0 24 24" aria-hidden="true">
            <rect x="2" y="5" width="20" height="14" fill="var(--brand-green)"/>
            <path d="M2 5l10 8 10-8" fill="none" stroke="var(--paper)" stroke-width="1.6"/>
          </svg>
          doreenvasquell@mailbrook.example
        </li>
      </ul>
    </div>
  </section>
</main>
</body>
</html>
```